Business card design needed

We need something on the back that allows the customer to get five stamps then the sixth visit they get 25 dollars to spend.
Industry/Entity Type
Business
Contact Information for Business Card
Quality meat,value for money,spit roast hire, wholesale pubs clubs,cater for bbqs.marlow lane butchery 217 marlow lane.64739204.

```html
<!DOCTYPE html>
<html lang="en">
<head>
<meta charset="utf-8">
<title>Marlow Lane Butchery – Business Card</title>
<link rel="stylesheet" href="https://fonts.googleapis.com/css2?family=Petit+Formal+Script&display=swap">
<style>
  :root {
    --page-bg: #ece9e4;
    --card-light: #eef0f2;
    --card-mid: #d4d7db;
    --card-dark: #b9bdc2;
    --globe-blue: #8ea3c4;
    --globe-green: #7d8f6a;
    --ink: #1b1b1b;
    --rule: #6c6f73;
    --stamp-fill: rgba(255,255,255,0.55);
  }
  * { box-sizing: border-box; margin: 0; padding: 0; }
  html, body {
    width: 1200px;
    height: 1200px;
    overflow: hidden;
    background: var(--page-bg);
  }
  .canvas {
    width: 1200px;
    height: 1200px;
    display: flex;
    flex-direction: column;
    align-items: center;
    justify-content: center;
    gap: 60px;
  }
  .card {
    position: relative;
    width: 880px;
    height: 503px;
    overflow: hidden;
    box-shadow: 0 4px 14px rgba(0,0,0,0.18);
    font-family: "Petit Formal Script", cursive;
    color: var(--ink);
  }
  .marble {
    position: absolute;
    inset: 0;
    background:
      radial-gradient(ellipse at 20% 30%, var(--card-dark) 0%, transparent 45%),
      radial-gradient(ellipse at 75% 70%, var(--card-mid) 0%, transparent 50%),
      radial-gradient(ellipse at 50% 10%, var(--card-light) 0%, transparent 55%),
      linear-gradient(135deg, var(--card-mid), var(--card-light) 50%, var(--card-mid));
  }
  .globe {
    position: absolute;
    top: 60px;
    right: -40px;
    width: 380px;
    height: 380px;
    border-radius: 50%;
    background: radial-gradient(circle at 40% 40%, var(--globe-green) 0%, var(--globe-blue) 55%, rgba(142,163,196,0) 72%);
    opacity: 0.75;
  }
  .fold-rule {
    position: absolute;
    top: 0;
    bottom: 0;
    left: 150px;
    width: 2px;
    background: var(--rule);
  }
  .card-text {
    position: absolute;
    left: 160px;
    right: 20px;
    top: 48px;
    text-align: center;
    font-size: 31px;
    line-height: 66px;
  }
  .loyalty {
    position: absolute;
    inset: 0;
    display: flex;
    flex-direction: column;
    align-items: center;
    justify-content: center;
    gap: 34px;
    text-align: center;
  }
  .loyalty-title { font-size: 34px; line-height: 48px; }
  .stamp-row {
    display: flex;
    gap: 26px;
  }
  .stamp {
    width: 100px;
    height: 100px;
    border-radius: 50%;
    border: 2px solid var(--rule);
    background: var(--stamp-fill);
    display: flex;
    align-items: center;
    justify-content: center;
    font-size: 28px;
  }
  .stamp-reward { border-width: 3px; border-color: var(--ink); font-size: 30px; }
  .loyalty-note { font-size: 26px; line-height: 40px; }
</style>
</head>
<body>
  <main class="canvas">
    <section class="card card-front">
      <div class="marble" role="img" aria-label="Soft grey marbled texture background"></div>
      <div class="globe" role="img" aria-label="Faded photograph of the earth from space"></div>
      <div class="fold-rule"></div>
      <div class="card-text">
        <p class="tagline">Quality meat, value for money,</p>
        <p class="services">Spit roast hire, wholesale pubs clubs,</p>
        <p class="services">cater for bbqs</p>
        <p class="business-name">Marlow lane butchery</p>
        <p class="address">217 Marlow lane</p>
        <p class="phone">64739204</p>
      </div>
    </section>
    <section class="card card-back">
      <div class="marble" role="img" aria-label="Soft grey marbled texture background"></div>
      <div class="loyalty">
        <p class="loyalty-title">Collect five stamps</p>
        <div class="stamp-row">
          <div class="stamp">1</div>
          <div class="stamp">2</div>
          <div class="stamp">3</div>
          <div class="stamp">4</div>
          <div class="stamp">5</div>
          <div class="stamp stamp-reward">$25</div>
        </div>
        <p class="loyalty-note">Your sixth visit gets $25 to spend</p>
      </div>
    </section>
  </main>
</body>
</html>
```